Swimming Pool Service Website needed!!!

Hi Everyone! Thanks for looking at my contest. I PROMISE to provide excellent feedback during this process.

I am starting a new swimming pool business cleaning company in San Diego, California and would like your help in making it similar to one of these two websites that are already functioning.

http://www.brightlagoonworks.example/services-repair.html

http://tidemarkaquacare.example/commercial-pool-cleaning.php

I like these two because they are easy to read, classy, sophisticated and have nice pictures of really clean & clear pools.

I really like the blue on white color format.

I do not have a logo, but the name of my company is GLIMMERWAVE POOL SERVICE.

My tag line is: Water so pure, it sparkles like a summer sky. (does not need to have the quotes around "in"...maybe just italics for this word IN?) You decide for me.

I would like to have a logo designed that incorporates some sort of easy to read letters. I do not want cursive (handwriting) letters. I thought about having a "reflection" of letters (mirror image), but think that this will be hard to read from far away. Maybe you can surprise me and come up with an idea that works using the a mirror image....but I'm not sure. I was leaning toward plain old BLOCK letters as I think it would be easy to read on my truck.

I would like to have 5 pages on my website:
1) Home
2) About Us (Know Your Poolman) / Why Hire Us
3) Services Offered
4) FAQ's
5) Contact

I am looking for a fully-functioning website (coded). Upon selection of the design winner, I am offering to increase the budget/payment by $100-$125 for the coding of all the pages. So anyone looking at participating in this contest, should be willing and able to provide the coding to the webpages that i've requested.

Target Market(s)

Upper middle-class homeowners who have a pool

Industry/Entity Type

Pool Service

Number of Pages Required

5+ page

Font styles to use
Serif

Colors
0455a3
3276b5
85acd3
85cae6
ffffff
33a6d7
0592cd

Requirements
Must have
• The Home page must have this picture highlighted in the top of the page:
• http://www.mesawaterpro.example/
• Must have pictures of some high-end pools. Any that you can find on the internet are wonderful.
• Must have a table on the right of the home page that mentions the service areas that we go to:
• • Carmel Valley (92130)
• • Del Mar (92014)
• • Rancho Santa Fe (92067)
• • Solana Beach (92075)
• • Santaluz (92127)
• • Cardiff (92007)
• • Encinitas (92024)
• • Carlsbad (92009, 92008)
• • La Jolla (92037)
• • Pacific Beach (92109)
• • Mira Mesa (92126)
• • Sorrento Valley (92121)
• • Clairemont (92117)
• • Rancho Bernardo (92127, 92128)
• • Rancho Penasquitos (92129)
• • Poway (92064)
• •
Nice to have
• Maybe incorporate some pictures of some kids (or families) playing in pools on the Why Hire Us page?
• I also like the feel of this website, but posting this page just for reference so you can get a feel more of what I like:
• http://www.crestlinepool.example/
• I like the FAQ's page from this website. I like how you can click on the question and then it pops up with the answer. http://www.dunewoodpoolcare.example/pool-spa-fountain-faqs/

```html
<!DOCTYPE html>
<html lang="en">
<head>
<meta charset="utf-8">
<title>Glimmerwave Pool Service</title>
<link rel="stylesheet" href="https://fonts.googleapis.com/css2?family=Arimo:wght@400;700&family=Carlito:wght@400;700&display=swap">
<style>
:root{
  --navy:#0b2f8a;
  --deep:#0455a3;
  --mid:#3276b5;
  --sky:#33a6d7;
  --bright:#0592cd;
  --pale:#85cae6;
  --soft:#85acd3;
  --white:#ffffff;
  --paper:#ebebeb;
  --footer:#2a5f99;
  --sun:#fff200;
}
*{box-sizing:border-box;margin:0;padding:0}
html,body{width:877px;height:1200px;overflow:hidden}
body{font-family:"Arimo",Arial,sans-serif;color:var(--white);position:relative;
  background:linear-gradient(#f4f4f4 0,#e2e2e2 388px,#3fa6e0 390px,#2f8fd5 560px,#2b7fcc 900px,#3b9ce0 1100px,#3a8fd4 1152px)}
.abs{position:absolute}
.brand{left:115px;top:36px;display:flex;align-items:center;gap:10px}
.brand-mark{width:92px;height:60px;border-radius:50%;background:var(--navy)}
.brand-name{font-family:"Arimo",Arial,sans-serif;font-weight:700;font-size:23px;line-height:24px;color:var(--navy);text-align:center}
.tagline{left:214px;top:86px;font-family:"Carlito",sans-serif;font-size:14px;color:#222}
.call{left:608px;top:56px;display:flex;align-items:center;gap:8px;font-family:"Carlito",sans-serif;font-size:12.5px;font-weight:700;color:var(--mid)}
.nav{left:110px;top:146px;width:658px;height:42px;background:linear-gradient(var(--sky),#2a8ccc);display:flex}
.nav a{color:var(--white);text-decoration:none;font-size:14px;line-height:42px;padding:0 17px;border-right:1px solid #1f74b0}
.nav a:first-child{padding:0 26px 0 40px}
.nav a.active{background:#3b9fda}
.nav a:last-child{border:none}
.dropdown{left:298px;top:185px;width:121px;height:142px;background:#3b9fda;border:1px solid #5fb5e6;padding:10px 0 0 9px;z-index:3}
.dropdown span{display:block;font-size:8.4px;line-height:24.3px;white-space:nowrap}
.hero{left:110px;top:188px;width:658px;height:253px;background:var(--white);padding:6px 4px;box-shadow:0 8px 14px rgba(0,0,0,.35)}
.hero-photo{width:100%;height:100%;background:linear-gradient(#5a8fb8 0,#8ab7cf 30%,#4f8a3f 42%,#7fa85a 55%,#6fb8cf 70%,#8fd0de 100%);position:relative}
.hero-line{position:absolute;right:78px;top:172px;text-align:center;font-weight:700;font-size:19px;line-height:24px;color:var(--sun);text-shadow:-1px -1px 0 #000,1px -1px 0 #000,-1px 1px 0 #000,1px 1px 0 #000}
.dots{position:absolute;left:32px;top:227px;display:flex;gap:4px}
.dots i{width:12px;height:12px;border-radius:50%;background:#e6eef3}
.signup{left:110px;top:465px;width:658px;height:54px;background:rgba(90,190,235,.55);display:flex;align-items:center;padding-left:20px;font-size:9.6px}
.btn{background:linear-gradient(#fbfbfb,#c9cfd5);border:1px solid #fff;border-radius:3px;color:var(--mid);font-family:"Carlito",sans-serif;text-align:center}
.signup .btn{position:absolute;left:387px;top:12px;width:184px;height:33px;line-height:31px;font-size:14px}
.service{top:542px;width:213px;height:139px;background:rgba(140,205,235,.6);border:1px solid #9fd8f0;border-radius:3px;padding:7px}
.service-photo{height:90px}
.service-label{position:absolute;left:0;right:0;top:110px;text-align:center;font-weight:700;font-size:11.5px}
.h2{font-family:"Carlito",sans-serif;font-size:16.5px;color:var(--navy)}
.welcome-photo{top:766px;width:145px;height:85px;border:1px solid #d8e6f2}
.copy{left:110px;top:872px;width:420px;font-family:"Carlito",sans-serif;font-size:9.2px;line-height:17px}
.copy p+p{margin-top:16px}
.readmore{left:110px;top:989px;width:99px;height:29px;line-height:27px;font-size:12px}
.calendar{left:556px;top:767px;width:212px;height:168px;background:#4fb0ea;border-radius:3px;padding:6px 4px}
.cal-grid{display:grid;grid-template-columns:repeat(7,28px);gap:1px;font-family:"Carlito",sans-serif}
.cal-grid .dow{font-size:11.5px;text-align:center;height:18px;color:#eaf6fd}
.cal-grid .day{height:25.5px;background:#7cc5ef;font-size:8.5px;color:var(--deep);padding:2px 0 0 4px}
.cal-grid .today{background:#a8e3fb}
.event{left:556px;top:945px;width:212px;height:72px;background:#4fb0ea;border-radius:3px;padding:12px 11px;font-family:"Carlito",sans-serif;color:var(--deep)}
.event h3{font-size:10.5px;font-weight:400;margin-bottom:11px}
.event p{font-size:8.6px;line-height:12.5px;color:#e8f6fd}
.clock{left:703px;top:1037px}
.footer{left:0;top:1152px;width:877px;height:48px;background:var(--footer);font-size:8.7px}
.footer span{position:absolute;top:18px}
.social{position:absolute;left:710px;top:15px;display:flex;gap:5px}
.social i{width:15px;height:15px;border-radius:50%;background:#c9dbee}
</style>
</head>
<body>

<div class="abs brand">
  <div class="brand-mark"></div>
  <div class="brand-name">GLIMMERWAVE POOL<br>SERVICE</div>
</div>
<div class="abs tagline">Water so pure, it sparkles like a summer sky</div>

<div class="abs call">
  <svg width="18" height="18" viewBox="0 0 18 18"><circle cx="9" cy="9" r="8" fill="none" stroke="#3276b5" stroke-width="1.3"/><path d="M6.5 5c-1 .8-1 2.5.6 4.6s3.3 3.3 4.4 2.6l.8-.9-1.6-1.4-.8.6c-.6-.2-1.6-1.3-1.9-1.9l.6-.8L7.3 4.3z" fill="#3276b5"/></svg>
  Call Us &nbsp;: &nbsp;0800 555 0142
</div>

<nav class="abs nav">
  <a href="#">Home</a><a href="#">About Us</a><a href="#" class="active">Service &amp; Repair</a><a href="#">Customer Reviews</a><a href="#">Contact Us</a>
</nav>
<div class="abs dropdown">
  <span>Automatic Pool Cleaners</span><span>Replacement Lines</span><span>Acid Washes</span><span>Light Repair and Installation</span><span>Mastic (expansion gap)</span>
</div>

<section class="abs hero">
  <div class="hero-photo" role="img" aria-label="Infinity pool by a lake with hills behind and a pool technician cleaning the water">
    <div class="hero-line">Bright Lagoon Works offers quality<br>pool repair &amp; services</div>
    <div class="dots"><i></i><i></i><i></i></div>
  </div>
</section>

<section class="abs signup">
  Lorem Ipsum has been the industry's standard dummy text ever since the 1500s,
  <div class="btn">Sign up Today</div>
</section>

<div class="abs service" style="left:110px">
  <div class="service-photo" role="img" aria-label="Pool edge with steel ladder and lounger" style="background:linear-gradient(#b8d8ef,#6cb4e2 45%,#2f86c8)"></div>
  <div class="service-label">SERVICE ONE</div>
</div>
<div class="abs service" style="left:333px">
  <div class="service-photo" role="img" aria-label="Tiled pool steps in clear blue water" style="background:linear-gradient(#4ca9df,#8ed3f0 50%,#3a97d6)"></div>
  <div class="service-label">SERVICE TWO</div>
</div>
<div class="abs service" style="left:556px">
  <div class="service-photo" role="img" aria-label="Stone pool corner with bright water" style="background:linear-gradient(110deg,#6b5a4a 0,#b79a7c 25%,#45b3e4 45%,#7fd2ef 100%)"></div>
  <div class="service-label">SERVICE THREE</div>
</div>

<h2 class="abs h2" style="left:110px;top:727px">Welcome to</h2>
<div class="abs welcome-photo" role="img" aria-label="Spa spilling into a blue pool" style="left:108px;background:linear-gradient(135deg,#2c6fa8,#5fb3e0 50%,#1d5f9c)"></div>
<div class="abs welcome-photo" role="img" aria-label="Backyard pool in front of a stone house" style="left:257px;background:linear-gradient(#c9c2b5 0,#8e8477 45%,#4fb6e6 60%,#2a8fd0)"></div>

<div class="abs copy">
  <p>We are Dublin based scuba diving school dedicated to teaching Scuba Diving in the internationally recognised ReefStar diving system. We have a real passion for diving and love everything about the real magic that the underwater world has to offer.</p>
  <p>We teach a range of courses starting from a very beginning right through to professional level diving. All our staffs are official Scuba Diving ReefStar, SafeDive instructors and ReefStar DiveMasters.</p>
</div>
<div class="abs btn readmore">Read More</div>

<h2 class="abs h2" style="left:556px;top:727px">Latest News</h2>
<div class="abs calendar">
  <div class="cal-grid">
    <div class="dow">Sun</div><div class="dow">Mon</div><div class="dow">Tue</div><div class="dow">Wed</div><div class="dow">Thur</div><div class="dow">Fri</div><div class="dow">Sat</div>
    <div class="day"></div><div class="day"></div><div class="day"></div><div class="day">1</div><div class="day">2</div><div class="day">3</div><div class="day">4</div>
    <div class="day">5</div><div class="day">6</div><div class="day">7</div><div class="day">8</div><div class="day">9</div><div class="day">10</div><div class="day">11</div>
    <div class="day">12</div><div class="day">13</div><div class="day">14</div><div class="day">15</div><div class="day today">16</div><div class="day">17</div><div class="day">18</div>
    <div class="day">5</div><div class="day">6</div><div class="day">7</div><div class="day">8</div><div class="day">9</div><div class="day">10</div><div class="day">11</div>
    <div class="day">26</div><div class="day">27</div><div class="day">28</div><div class="day">29</div><div class="day">30</div><div class="day"></div><div class="day"></div>
  </div>
</div>
<div class="abs event">
  <h3>15 - 17 February</h3>
  <p>Stop by ReefStar Booth #507 at the Harborview Expo Hall, Lakemont, Oregon,</p>
</div>

<svg class="abs clock" width="64" height="64" viewBox="0 0 64 64" aria-label="Clock">
  <circle cx="32" cy="32" r="31" fill="#d9dee3" stroke="#aab3bc"/>
  <circle cx="32" cy="32" r="26" fill="#f7f8f9" stroke="#c4ccd3"/>
  <g stroke="#555" stroke-width="1.2">
    <line x1="32" y1="8" x2="32" y2="11"/><line x1="32" y1="53" x2="32" y2="56"/>
    <line x1="8" y1="32" x2="11" y2="32"/><line x1="53" y1="32" x2="56" y2="32"/>
  </g>
  <line x1="32" y1="32" x2="32" y2="13" stroke="#333" stroke-width="1.5"/>
  <line x1="32" y1="32" x2="47" y2="32" stroke="#333" stroke-width="2"/>
  <circle cx="32" cy="32" r="2" fill="#333"/>
</svg>

<footer class="abs footer">
  <span style="left:110px">&copy; All Right Reserved | Privacy Policy</span>
  <span style="left:363px">Terms &amp; Condition &nbsp;&nbsp; | &nbsp;&nbsp; Privacy Policy</span>
  <span style="left:646px">Social Media</span>
  <div class="social"><i></i><i></i><i></i></div>
  <span style="left:835px">C4</span>
</footer>

</body>
</html>
```